deceased estate cleaning services and cosmetic renovating

house frontage signage design
cur flute sign will be 600mm x 450 mm and no larger
is to be mounted of fence out front of projects as advertizing

Target Market(s)

elderly people and there sibling that need help

Colors
cadf82
85cae6
fbed22
85acd3
ffcf3e

Requirements
Must have
• clear phone number, email and business Name and logo
Should not have
• to much info and NO dark colors

```html
<!DOCTYPE html>
<html lang="en">
<head>
<meta charset="utf-8">
<title>TIDYNEST – De-clutter Your Life sign</title>
<link rel="stylesheet" href="https://fonts.googleapis.com/css2?family=Anton&family=Montserrat:wght@500;600;700;800&display=swap">
<style>
  :root {
    --sky-light: #b4e6fb;
    --sky: #85cae6;
    --sky-deep: #7fd2f5;
    --green-dark: #5fa64f;
    --green-light: #cadf82;
    --green-lime: #b5d45a;
    --grass: #7fb850;
    --grass-light: #a4cc68;
    --ink: #141414;
    --red: #e00000;
    --white: #ffffff;
    --footer: #bcc7c9;
    --footer-edge: #a9b6b8;
  }
  * { box-sizing: border-box; margin: 0; padding: 0; }
  html, body { width: 1200px; height: 945px; overflow: hidden; background: #f2f2f2; }
  .sign {
    position: relative;
    width: 1200px; height: 945px;
    overflow: hidden;
    background: radial-gradient(ellipse at 70% 45%, var(--sky-light) 0%, var(--sky-deep) 70%, var(--sky) 100%);
    font-family: "Montserrat", Arial, sans-serif;
  }
  .top-bands { position: absolute; left: 0; top: 0; width: 1200px; height: 44px; }
  .grass {
    position: absolute; left: 0; top: 771px; width: 1200px; height: 101px;
    background: linear-gradient(180deg, var(--grass-light) 0%, var(--grass) 100%);
  }
  .headline {
    position: absolute; left: 0; top: 0; width: 720px; height: 320px;
    overflow: visible;
  }
  .headline text {
    font-family: "Anton", Impact, sans-serif;
    font-size: 108px;
    filter: drop-shadow(4px 4px 0 var(--white));
  }
  .headline .line-one { fill: var(--ink); }
  .headline .line-two { fill: var(--red); }
  .brand-name {
    position: absolute; left: 740px; top: 241px; width: 334px;
    text-align: center; line-height: 1;
    font-size: 62px; font-weight: 600; letter-spacing: 1px;
    color: var(--ink);
  }
  .values {
    position: absolute; left: 82px; top: 326px; width: 1036px; height: 89px;
    border-radius: 10px;
    background: linear-gradient(90deg, var(--green-dark) 0%, var(--green-lime) 100%);
    color: var(--white); font-weight: 800; font-size: 43px;
  }
  .values .item { position: absolute; top: 0; height: 89px; display: flex; align-items: center; white-space: nowrap; }
  .values .chev { font-weight: 600; margin-right: 8px; }
  .values .quality { left: 50px; }
  .values .pride { left: 318px; }
  .values .professionalism { left: 522px; }
  .help-title {
    position: absolute; left: 344px; top: 448px;
    line-height: 1;
    font-size: 40px; font-weight: 700; letter-spacing: 0.5px; color: var(--ink);
    white-space: nowrap;
  }
  .query-bubble { position: absolute; left: 424px; top: 530px; width: 366px; height: 92px; }
  .query-line { position: absolute; left: 424px; width: 366px; text-align: center; color: var(--ink); line-height: 1; white-space: nowrap; }
  .query-soft { top: 542px; font-size: 22px; font-weight: 500; }
  .query-bold { top: 566px; font-size: 26px; font-weight: 700; }
  .contact { position: absolute; left: 428px; width: 360px; display: flex; align-items: center; justify-content: space-between; color: var(--red); line-height: 1; white-space: nowrap; }
  .contact svg { flex: none; }
  .contact-email { top: 632px; font-size: 28.5px; font-weight: 500; }
  .contact-phone { top: 673px; font-size: 45px; font-weight: 800; letter-spacing: 0.5px; }
  .contact-web { top: 726px; font-size: 29px; font-weight: 500; }
  .scene-art {
    position: absolute; left: 22px; top: 498px; width: 400px; height: 370px;
    background: linear-gradient(180deg, rgba(190,230,250,0.6) 0%, rgba(200,160,140,0.55) 45%, rgba(140,190,90,0.7) 100%);
    border-radius: 6px;
  }
  .recycle-art {
    position: absolute; left: 832px; top: 498px; width: 310px; height: 344px;
    background: radial-gradient(circle at 50% 46%, #ffffff 0%, #9ad46a 30%, rgba(90,110,120,0.55) 55%, rgba(180,225,245,0.3) 75%);
    border-radius: 50%;
  }
  .footer-line { position: absolute; left: 0; top: 872px; width: 1200px; height: 8px; background: var(--white); }
  .footer {
    position: absolute; left: 0; top: 880px; width: 1200px; height: 65px;
    background: linear-gradient(180deg, var(--footer) 0%, var(--footer-edge) 100%);
    display: flex; align-items: center; justify-content: space-between;
    padding: 0 105px 0 48px;
    font-size: 22.5px; font-weight: 700; letter-spacing: 0.5px; color: var(--ink);
  }
</style>
</head>
<body>
<main class="sign">
  <svg class="top-bands" viewBox="0 0 1200 44" aria-hidden="true">
    <polygon points="0,0 665,0 643,43 0,43" fill="var(--green-dark)"/>
    <polygon points="670,0 1200,0 1200,16 662,16" fill="var(--white)"/>
    <polygon points="682,0 1200,0 1200,15 674,15" fill="var(--green-lime)"/>
  </svg>

  <div class="grass"></div>

  <svg class="headline" viewBox="0 0 720 320" role="heading" aria-level="1" aria-label="De-clutter your life">
    <g transform="translate(0,189) skewX(-9)">
      <text class="line-one" x="105" y="0" textLength="556" lengthAdjust="spacingAndGlyphs">DE-CLUTTER</text>
    </g>
    <g transform="translate(0,302) skewX(-9)">
      <text class="line-two" x="103" y="0" textLength="534" lengthAdjust="spacingAndGlyphs">YOUR LIFE</text>
    </g>
  </svg>

  <div class="brand-name">TIDYNEST</div>

  <div class="values">
    <span class="item quality"><span class="chev">»</span>QUALITY</span>
    <span class="item pride"><span class="chev">»</span>PRIDE</span>
    <span class="item professionalism"><span class="chev">»</span>PROFESSIONALISM</span>
  </div>

  <h2 class="help-title">WE ARE HERE TO HELP</h2>

  <svg class="query-bubble" viewBox="0 0 366 92" aria-hidden="true">
    <path d="M6,1 H360 a5,5 0 0 1 5,5 V67 a5,5 0 0 1 -5,5 H212 L194,88 L198,72 H6 a5,5 0 0 1 -5,-5 V6 a5,5 0 0 1 5,-5 Z" fill="none" stroke="var(--red)" stroke-width="1.5"/>
  </svg>
  <p class="query-line query-soft">IF YOU HAVE ANY QUERIES,</p>
  <p class="query-line query-bold">GET IN TOUCH WITH US</p>

  <div class="contact contact-email">
    <svg width="28" height="20" viewBox="0 0 28 20" aria-hidden="true"><rect x="1" y="1" width="26" height="18" fill="none" stroke="var(--ink)" stroke-width="1.6"/><path d="M1,1 L14,11 L27,1 M1,19 L10,9 M27,19 L18,9" fill="none" stroke="var(--ink)" stroke-width="1.6"/></svg>
    <span>info@tidynest.com.au</span>
  </div>
  <div class="contact contact-phone">
    <svg width="36" height="36" viewBox="0 0 36 36" aria-hidden="true"><circle cx="18" cy="18" r="16" fill="none" stroke="var(--ink)" stroke-width="2"/><path d="M12,9 l4,0 l1,6 l-3,2 c1,3 3,5 6,6 l2,-3 l6,1 l0,4 c-10,1 -17,-7 -16,-16 z" fill="none" stroke="var(--ink)" stroke-width="1.8"/></svg>
    <span>0400 123 456</span>
  </div>
  <div class="contact contact-web">
    <svg width="24" height="24" viewBox="0 0 24 24" aria-hidden="true"><g fill="none" stroke="var(--ink)" stroke-width="1.6"><circle cx="12" cy="12" r="10.5"/><ellipse cx="12" cy="12" rx="4.5" ry="10.5"/><path d="M1.5,12 H22.5 M3.5,6.5 H20.5 M3.5,17.5 H20.5"/></g></svg>
    <span>www.tidynest.com.au</span>
  </div>

  <div class="scene-art" role="img" aria-label="Illustration of a house overflowing with household clutter, a removal truck with its driver, clouds, sun and a white picket fence"></div>
  <div class="recycle-art" role="img" aria-label="Glowing green recycling symbol surrounded by a ring of life-stage silhouettes from birth to old age"></div>

  <div class="footer-line"></div>
  <footer class="footer">
    <span>COSMETIC REPAIRS AND HOUSE MAINTENANCE</span>
    <span>RECYCLE OUR LIFE</span>
  </footer>
</main>
</body>
</html>
```